Need Bold, Hip Card for Concert Ticket Website Gleaming Passes!

Hi there! I am putting together a business/website that sells event tickets (mostly concerts, but also some sports and theater). Think SeatNook, but much smaller. The site is called Gleaming Passes. I have a new logo (attached, with black/red/white color scheme), and am looking for a modern/cool/original business card design. Note that I am thinking of having the card itself in the shape of a ticket (die cut), so you may want to keep that in mind when designing, but I'm not set on that. I'm also open to alternative card sizes, thicknesses, glossy, spot UV, etc. in order to stand out. I'm attaching a potential die cut template and a sample card using that template in case you want to work with that.
Target Market(s)
Music fans, people that like going to see live events
Industry/Entity Type
Entertainment
Contact Information for Business Card
Information that I'd like to have:
website address - www.gleamingpasses.example
phone number: 1-833-5GLEAMNG (532-6264)
my name - Wendel Pike

```html
<!DOCTYPE html>
<html lang="en">
<head>
<meta charset="utf-8">
<title>Gleaming Passes – Business Card</title>
<link href="https://fonts.googleapis.com/css2?family=Montserrat:wght@600;700&family=Roboto:wght@700&display=swap" rel="stylesheet">
<style>
  :root {
    --backdrop: #696969;
    --card-dark: #0b0b0c;
    --card-light: #f8f8f8;
    --brand-red: #8e1515;
    --ink: #1b1b1b;
    --mark-grey: #7c7c7c;
  }
  html, body {
    margin: 0;
    padding: 0;
    width: 1200px;
    height: 590px;
    overflow: hidden;
    background: var(--backdrop);
  }
  .stage {
    position: relative;
    width: 1200px;
    height: 590px;
  }
  .ticket-card {
    position: absolute;
    top: 154px;
    width: 491px;
    height: 280px;
  }
  .ticket-card--front { left: 94px; }
  .ticket-card--back { left: 614px; }
  .ticket-shape {
    position: absolute;
    inset: 0;
    width: 491px;
    height: 280px;
  }
  .ticket-shape--dark path { fill: var(--card-dark); }
  .ticket-shape--light path { fill: var(--card-light); }
  .ticket-shape line {
    stroke: var(--brand-red);
    stroke-width: 1.6;
    stroke-dasharray: 4 4;
  }
  .brand-name {
    position: absolute;
    display: flex;
    align-items: center;
    gap: 12px;
    font-family: "Montserrat", sans-serif;
    font-weight: 700;
    text-transform: uppercase;
    line-height: 1;
  }
  .brand-name__square {
    width: 30px;
    height: 30px;
    flex: none;
  }
  .brand-name__words span { display: block; }
  .brand-name--front {
    left: 110px;
    top: 98px;
    color: var(--mark-grey);
  }
  .brand-name--front .brand-name__square { background: var(--mark-grey); width: 44px; height: 44px; }
  .brand-name--front .brand-name__top { font-size: 40px; letter-spacing: 1px; }
  .brand-name--front .brand-name__bottom { font-size: 30px; letter-spacing: 13px; margin-top: 6px; }
  .brand-name--back {
    right: 43px;
    top: 44px;
    color: var(--brand-red);
  }
  .brand-name--back .brand-name__square { background: var(--brand-red); }
  .brand-name--back .brand-name__top { font-size: 28px; letter-spacing: 0.5px; }
  .brand-name--back .brand-name__bottom { font-size: 21px; letter-spacing: 8.6px; margin-top: 4px; }
  .contact {
    position: absolute;
    left: 53px;
    top: 184px;
  }
  .contact__name {
    margin: 0 0 10px;
    font-family: "Montserrat", sans-serif;
    font-weight: 600;
    font-size: 21px;
    letter-spacing: 1px;
    color: var(--brand-red);
    text-transform: uppercase;
  }
  .contact__line {
    margin: 0 0 3px;
    font-family: "Roboto", sans-serif;
    font-weight: 700;
    font-size: 12.5px;
    color: var(--ink);
  }
</style>
</head>
<body>
<main class="stage">
  <section class="ticket-card ticket-card--front">
    <svg class="ticket-shape ticket-shape--dark" viewBox="0 0 491 280" aria-hidden="true">
      <path d="M32 0 H459 A32 32 0 0 0 491 32 V248 A32 32 0 0 0 459 280 H32 A32 32 0 0 0 0 248 V32 A32 32 0 0 0 32 0 Z"/>
    </svg>
    <div class="brand-name brand-name--front">
      <div class="brand-name__square"></div>
      <div class="brand-name__words">
        <span class="brand-name__top">Gleaming</span>
        <span class="brand-name__bottom">Passes</span>
      </div>
    </div>
  </section>

  <section class="ticket-card ticket-card--back">
    <svg class="ticket-shape ticket-shape--light" viewBox="0 0 491 280" aria-hidden="true">
      <path d="M32 0 H459 A32 32 0 0 0 491 32 V248 A32 32 0 0 0 459 280 H32 A32 32 0 0 0 0 248 V32 A32 32 0 0 0 32 0 Z"/>
      <line x1="53" y1="16" x2="438" y2="16"/>
      <line x1="53" y1="264" x2="438" y2="264"/>
    </svg>
    <div class="brand-name brand-name--back">
      <div class="brand-name__square"></div>
      <div class="brand-name__words">
        <span class="brand-name__top">Gleaming</span>
        <span class="brand-name__bottom">Passes</span>
      </div>
    </div>
    <div class="contact">
      <h1 class="contact__name">Wendel Pike</h1>
      <p class="contact__line">1-833-5GLEAMNG (532-6264)</p>
      <p class="contact__line">www.gleamingpasses.example</p>
    </div>
  </section>
</main>
</body>
</html>
```